Business Card Design Project

We are not a new company, but renamed to "Norvanta Kitchens" last year. We specialize in modern high-end cabinetry imports. We would like to communicate a sense of quality and cutting edge technology. Ideally the design would incorporate our logo colors, silver, red and preferably a black, matte background. Though we are open to suggestions.
Logo is attached.
Edit: I have attached rough drafts of the previous cards, this way you will have all necessary content that needs to go on the cards.
Reason: We have received a lot of great designs, but due to the sheer number we couldn't respond to all. We will extend the deadline for another 7 days to finalize and provide feedback to designers.
Thank you for your hard work!
Industry/Entity Type
Business
Look and feel
Each slider illustrates characteristics of the customer's brand and the style your logo design should communicate.

```html
<!DOCTYPE html>
<html lang="en">
<head>
<meta charset="utf-8">
<title>Norvanta Kitchens – Business Card</title>
<link rel="stylesheet" href="https://fonts.googleapis.com/css2?family=Michroma&family=Arimo:wght@400&display=swap">
<style>
  :root {
    --page-bg: #e9e9ee;
    --card-dark: #2a2a2c;
    --card-dark-deep: #1b1b1d;
    --silver: #c9cacd;
    --panel-grey: #c7c8cb;
    --stripe-dark: #2f2f31;
    --accent-red: #e0202a;
    --ink-light: #e6e6e8;
    --ink-dark: #1e1e20;
  }
  * { margin: 0; padding: 0; box-sizing: border-box; }
  html, body { width: 1200px; height: 987px; overflow: hidden; }
  body {
    background: var(--page-bg);
    display: flex;
    flex-direction: column;
    align-items: center;
    justify-content: center;
    gap: 32px;
    font-family: "Arimo", Arial, sans-serif;
  }
  .card {
    position: relative;
    width: 780px;
    height: 446px;
    border-radius: 26px;
    overflow: hidden;
    background: linear-gradient(150deg, var(--card-dark) 0%, var(--card-dark-deep) 100%);
    box-shadow: 0 6px 18px rgba(0,0,0,0.18);
  }
  .card__swoosh { position: absolute; inset: 0; width: 100%; height: 100%; }
  .wordmark {
    font-family: "Michroma", sans-serif;
    font-weight: 400;
    color: var(--silver);
    text-transform: uppercase;
    white-space: nowrap;
  }
  .front .wordmark {
    position: absolute;
    left: 62px;
    top: 96px;
    font-size: 40px;
    letter-spacing: 1px;
  }
  .holder {
    position: absolute;
    left: 64px;
    top: 168px;
    font-family: "Michroma", sans-serif;
    font-size: 17px;
    letter-spacing: 4px;
    color: var(--ink-light);
    text-transform: uppercase;
  }
  .holder__role { color: var(--accent-red); }
  .contacts {
    position: absolute;
    left: 64px;
    top: 208px;
    list-style: none;
    color: var(--ink-light);
    font-size: 16px;
    line-height: 29px;
  }
  .contacts li { display: flex; align-items: center; gap: 8px; }
  .contacts svg { width: 14px; height: 14px; fill: var(--accent-red); flex: none; }
  .address {
    position: absolute;
    right: 44px;
    bottom: 34px;
    text-align: right;
    font-style: normal;
    color: var(--ink-dark);
    font-size: 19px;
    line-height: 27px;
  }
  .back { display: flex; align-items: center; justify-content: center; }
  .back .wordmark { font-size: 38px; letter-spacing: 1px; text-align: center; }
</style>
</head>
<body>

  <section class="card front">
    <svg class="card__swoosh" viewBox="0 0 780 446" preserveAspectRatio="none" aria-hidden="true">
      <path d="M0,300 C140,365 300,352 480,342 C620,334 720,312 780,302 L780,446 L0,446 Z" fill="var(--panel-grey)"/>
      <path d="M0,282 C140,345 300,334 480,324 C620,316 720,294 780,284 L780,296 C720,306 620,328 480,336 C300,346 140,358 0,296 Z" fill="var(--stripe-dark)"/>
    </svg>

    <h1 class="wordmark">Norvanta Kitchens</h1>

    <p class="holder">Mattias Holm, <span class="holder__role">Director</span></p>

    <ul class="contacts">
      <li>
        <svg viewBox="0 0 24 24" aria-hidden="true"><path d="M6.6 10.8a15.1 15.1 0 0 0 6.6 6.6l2.2-2.2c.3-.3.7-.4 1-.2 1.1.4 2.3.6 3.6.6.6 0 1 .4 1 1V20c0 .6-.4 1-1 1A17 17 0 0 1 3 4c0-.6.4-1 1-1h3.5c.6 0 1 .4 1 1 0 1.3.2 2.5.6 3.6.1.3 0 .7-.2 1z"/></svg>
        780.555.0142
      </li>
      <li>
        <svg viewBox="0 0 24 24" aria-hidden="true"><path d="M5 9h14v9H5zM7 5h10l2 4H5zM7 18v2M17 18v2" stroke="var(--accent-red)" stroke-width="2"/></svg>
        780.555.0187
        <svg viewBox="0 0 24 24" aria-hidden="true"><path d="M7 2h10a1 1 0 0 1 1 1v18a1 1 0 0 1-1 1H7a1 1 0 0 1-1-1V3a1 1 0 0 1 1-1zm1 3v12h8V5z"/></svg>
        780.555.0163
      </li>
      <li>
        <svg viewBox="0 0 24 24" aria-hidden="true"><path d="M3 5h18v14H3zm2 2v.5l7 5 7-5V7l-7 5z"/></svg>
        mattias@norvantakitchens.ca
      </li>
    </ul>

    <address class="address">2186 - 84 St. Edmonton<br>AB T5X 2K9</address>
  </section>

  <section class="card back">
    <h2 class="wordmark">Norvanta Kitchens</h2>
  </section>

</body>
</html>
```